Halvern Institute Seminar Series Flyer

I am looking to update our Halvern Institute flyer. Please take a look at the our current version attached and feel free to revise as you see fit. I would like something eye catching, but not to busy. I am attaching the epigenetics logo as well. It would be great if you could use the logo and take out the white background in the logo to fit in seamlessly within the flyer.

Target Market(s)

Medical Doctors and Scientist

```html
<!DOCTYPE html>
<html lang="en">
<head>
<meta charset="utf-8">
<title>Halvern Institute Seminar Series</title>
<link href="https://fonts.googleapis.com/css2?family=Montserrat:wght@500;600;700&family=Oswald:wght@600;700&display=swap" rel="stylesheet">
<style>
  :root {
    --navy: #0f4272;
    --navy-deep: #0b3560;
    --helix-light: #5ba4e6;
    --helix-mid: #2b7fd0;
    --heading-blue: #1a4e86;
    --accent-red: #c8102e;
    --text-dark: #333336;
    --rule: #d4d8de;
    --paper-top: #e8f1fa;
    --paper: #ffffff;
  }
  html, body {
    margin: 0;
    padding: 0;
    width: 960px;
    height: 1200px;
    overflow: hidden;
    background: var(--paper);
  }
  .flyer {
    position: relative;
    width: 960px;
    height: 1200px;
    overflow: hidden;
    background: linear-gradient(180deg, var(--paper-top) 0%, var(--paper) 48%);
    font-family: "Montserrat", Arial, sans-serif;
  }
  .backdrop {
    position: absolute;
    inset: 0;
  }
  .masthead {
    position: absolute;
    left: 39px;
    top: 50px;
    color: #fff;
  }
  .masthead__university {
    font-weight: 700;
    font-size: 17px;
    letter-spacing: 0.2px;
    margin: 0 0 18px;
  }
  .masthead__name {
    font-family: "Oswald", "Arial Narrow", sans-serif;
    font-weight: 700;
    font-size: 92px;
    line-height: 0.95;
    margin: 0;
    letter-spacing: -1px;
  }
  .masthead__sub {
    font-family: "Oswald", "Arial Narrow", sans-serif;
    font-weight: 700;
    font-size: 56px;
    line-height: 1;
    margin: 2px 0 0;
  }
  .masthead__series {
    font-family: "Oswald", "Arial Narrow", sans-serif;
    font-weight: 600;
    font-size: 41px;
    line-height: 1;
    margin: 38px 0 0;
    letter-spacing: -0.5px;
  }
  .institute-mark {
    position: absolute;
    left: 712px;
    top: 318px;
    display: flex;
    align-items: center;
    gap: 10px;
    font-weight: 700;
    font-size: 22px;
    color: var(--heading-blue);
  }
  .institute-mark__dot {
    width: 22px;
    height: 22px;
    border-radius: 50%;
    background: var(--accent-red);
  }
  .program {
    position: absolute;
    left: 518px;
    top: 468px;
    width: 420px;
  }
  .speaker__name {
    font-weight: 700;
    color: var(--heading-blue);
    margin: 0;
    line-height: 1.12;
  }
  .speaker__name--lead { font-size: 39px; }
  .speaker__name--second { font-size: 30px; margin-top: 48px; }
  .speaker__role {
    font-weight: 600;
    font-size: 22px;
    color: var(--text-dark);
    margin: 14px 0 0;
    line-height: 1.3;
  }
  .speaker__talk {
    font-weight: 600;
    color: var(--accent-red);
    margin: 14px 0 0;
    line-height: 1.27;
  }
  .speaker__talk--lead { font-size: 23px; }
  .speaker__talk--second { font-size: 19.5px; margin-top: 16px; line-height: 1.25; }
  .details {
    list-style: none;
    margin: 0;
    padding: 0;
    position: absolute;
    left: 518px;
    top: 930px;
    width: 380px;
  }
  .details li {
    font-weight: 600;
    font-size: 18.5px;
    color: var(--text-dark);
    padding: 8px 0 9px;
    border-bottom: 1px solid var(--rule);
  }
  .details li:last-child { border-bottom: none; }
  .contact {
    position: absolute;
    left: 33px;
    top: 1040px;
    font-weight: 600;
    font-size: 16.5px;
    line-height: 25.5px;
    color: var(--text-dark);
    margin: 0;
  }
  .sponsor {
    position: absolute;
    left: 521px;
    top: 1092px;
  }
  .sponsor__label {
    font-weight: 600;
    font-size: 16px;
    color: #555;
    margin: 0 0 12px;
  }
  .sponsor__name {
    display: flex;
    align-items: center;
    gap: 8px;
    font-weight: 700;
    font-size: 24px;
    letter-spacing: 2px;
    color: #1f4d2a;
  }
  .sponsor__square {
    width: 22px;
    height: 22px;
    background: #e0b21a;
  }
</style>
</head>
<body>
<main class="flyer">
  <svg class="backdrop" width="960" height="1200" viewBox="0 0 960 1200" aria-hidden="false">
    <defs>
      <linearGradient id="helixTone" x1="0" y1="0" x2="1" y2="1">
        <stop offset="0" stop-color="var(--helix-light)"/>
        <stop offset="0.5" stop-color="var(--helix-mid)"/>
        <stop offset="1" stop-color="var(--helix-light)"/>
      </linearGradient>
    </defs>
    <polygon class="backdrop__panel" points="0,0 650,0 0,995" fill="var(--navy)"/>
    <g role="img" aria-label="Illustration of a blue DNA double helix running diagonally across the flyer">
      <polygon points="560,0 760,0 120,1010 0,1010 0,900" fill="url(#helixTone)" opacity="0.9"/>
    </g>
  </svg>

  <header class="masthead">
    <p class="masthead__university">NORTHBROOK UNIVERSITY</p>
    <h1 class="masthead__name">HALVERN</h1>
    <p class="masthead__sub">INSTITUTE</p>
    <p class="masthead__series">SEMINAR SERIES</p>
  </header>

  <div class="institute-mark">
    <span class="institute-mark__dot"></span>
    <span>Halvern Institute</span>
  </div>

  <section class="program">
    <article class="speaker">
      <h2 class="speaker__name speaker__name--lead">Martin K. Ellery, PHD</h2>
      <p class="speaker__role">Assistant Professor of Genetics</p>
      <p class="speaker__role">Aldine School of Medicine<br>at Northbrook University</p>
      <p class="speaker__talk speaker__talk--lead">Dissecting the molecular basis<br>of chromosome positioning</p>
    </article>
    <article class="speaker">
      <h2 class="speaker__name speaker__name--second">Clara Whitfield<br>(Dorsey Lab)</h2>
      <p class="speaker__talk speaker__talk--second">Exploiting DNA Deaminases to Localize<br>5-hydroxymethylcytosine in Genome</p>
    </article>
  </section>

  <ul class="details">
    <li>Date: Thursday, March 9, 2017</li>
    <li>Time: 4.00 PM</li>
    <li>Location: 9-146 Kessler Center</li>
  </ul>

  <p class="contact">
    For more information contact<br>
    Renata Alvarez-Moore<br>
    at ramoore@northbrook.edu<br>
    or go to our website:<br>
    www.halvern.med.northbrook.edu
  </p>

  <aside class="sponsor">
    <p class="sponsor__label">Thanks to our Sponsor</p>
    <div class="sponsor__name">
      <span class="sponsor__square"></span>
      <span>GENOVANCE</span>
    </div>
  </aside>
</main>
</body>
</html>
```